Business card design needed

Black on pure white.
Two coloured logos.
Text/info on back

Varnex Logo Attached

Industry/Entity Type

Business

Contact Information for Business Card

Brightway Portals Pty. Ltd.
Varnex Quorlind High Speed Doors.
Gordon T. Ashby
0491 658203
sales@brightwayportals.com.au
www.brightwayportals.com.au

Logo styles of interest
Abstract Logo

```html
<!DOCTYPE html>
<html lang="en">
<head>
<meta charset="utf-8">
<title>Brightway Portals – Business Card</title>
<link href="https://fonts.googleapis.com/css2?family=Josefin+Sans:wght@300;400&display=swap" rel="stylesheet">
<style>
  :root {
    --ink: #111111;
    --paper: #ffffff;
    --backdrop: #d9d8d6;
    --logo-green: #4caf3a;
    --logo-red: #d8262c;
  }
  * { box-sizing: border-box; margin: 0; padding: 0; }
  html, body {
    width: 1200px; height: 900px; overflow: hidden;
    background: var(--backdrop);
    font-family: "Josefin Sans", "Helvetica Neue", Arial, sans-serif;
    color: var(--ink);
  }
  .sheet {
    width: 1200px; height: 900px;
    display: flex; align-items: center; justify-content: center; gap: 90px;
  }
  .card {
    width: 340px; height: 595px;
    background: var(--paper);
    position: relative;
  }

  /* Front side */
  .card--front { display: flex; flex-direction: column; align-items: center; justify-content: center; }
  .logo-frame {
    width: 170px; height: 170px;
    border: 3px solid var(--ink);
    display: flex; flex-direction: column; align-items: center; justify-content: center; gap: 16px;
  }
  .brand {
    display: flex; align-items: center; gap: 7px;
    font-size: 15px; font-weight: 400; letter-spacing: 0.04em; text-transform: uppercase;
  }
  .brand__mark { flex: none; }
  .brand--primary { color: var(--logo-green); }
  .brand--partner { color: var(--logo-red); }
  .origin-note {
    margin-top: 12px;
    font-size: 8px; font-weight: 400; letter-spacing: 0.06em;
  }

  /* Back side */
  .card--back { padding: 70px 0 0 58px; }
  .name-box {
    width: 168px;
    border: 3px solid var(--ink);
    padding: 14px 14px 12px;
  }
  .name-box__first { font-size: 27px; font-weight: 400; letter-spacing: 0.02em; line-height: 1; }
  .name-box__last { font-size: 22px; font-weight: 300; line-height: 1.1; margin-top: 4px; }
  .name-box__divider {
    display: flex; align-items: center; gap: 8px; margin: 10px 0 8px;
    font-size: 9px;
  }
  .name-box__divider::before, .name-box__divider::after {
    content: ""; flex: 1; height: 1px; background: var(--ink);
  }
  .name-box__role { font-size: 11px; font-weight: 300; letter-spacing: 0.06em; }
  .rule { width: 226px; height: 3px; background: var(--ink); }
  .rule--name { margin-top: 16px; }
  .phone {
    margin: 10px 0 8px;
    font-size: 41px; font-weight: 300; line-height: 0.92; letter-spacing: 0.02em;
  }
  .contact-line { padding: 7px 0 9px; font-size: 11px; line-height: 1.35; }
  .contact-line__label { font-weight: 400; letter-spacing: 0.08em; }
  .contact-line__value { font-weight: 300; letter-spacing: 0.03em; }
</style>
</head>
<body>
<main class="sheet">
  <section class="card card--front" aria-label="Card front">
    <div class="logo-frame">
      <div class="brand brand--primary">
        <svg class="brand__mark" width="12" height="12" viewBox="0 0 12 12" aria-hidden="true"><circle cx="6" cy="6" r="6" fill="currentColor"/></svg>
        <span>Brightway Portals</span>
      </div>
      <div class="brand brand--partner">
        <svg class="brand__mark" width="11" height="11" viewBox="0 0 11 11" aria-hidden="true"><rect width="11" height="11" fill="currentColor"/></svg>
        <span>Varnex</span>
      </div>
    </div>
    <p class="origin-note">★ built in australia</p>
  </section>

  <section class="card card--back" aria-label="Card back">
    <div class="name-box">
      <p class="name-box__first">GORDON</p>
      <p class="name-box__last">T. Ashby</p>
      <p class="name-box__divider">★</p>
      <p class="name-box__role">SALES MANAGER</p>
    </div>
    <div class="rule rule--name"></div>
    <p class="phone">+0<br>491<br>658<br>203</p>
    <div class="rule"></div>
    <p class="contact-line">
      <span class="contact-line__label">SALES@</span><br>
      <span class="contact-line__value">brightwayportals.com.au</span>
    </p>
    <div class="rule"></div>
    <p class="contact-line">
      <span class="contact-line__label">WEBSITE</span><br>
      <span class="contact-line__value">brightwayportals.com.au</span>
    </p>
    <div class="rule"></div>
  </section>
</main>
</body>
</html>
```